Facebook Page Design for a Medical Billing Business

We need help designing a facebook page that is professional, yet friendly that will attract medical practitioners (doctors, therapists, nutritionists, chiropractors, etc) to check out and follow our business. I have attached our logo which must be incorporated in the design.

```html
<!DOCTYPE html>
<html lang="en">
<head>
<meta charset="utf-8">
<title>Vega Claims Billing – Page Cover</title>
<link rel="stylesheet" href="https://fonts.googleapis.com/css2?family=Anton&family=Tinos:ital,wght@0,400;1,700&display=swap">
<style>
  :root {
    --page-bg: #2a3038;
    --cover-white: #ffffff;
    --cover-mist: #eef0f4;
    --navy: #1d2a80;
    --plum: #7a3d94;
    --violet: #3a2a8c;
    --magenta: #9a3a98;
    --accent-blue: #1f63c4;
    --pink-rule: #c0479c;
  }
  html, body {
    margin: 0;
    width: 1039px;
    height: 1200px;
    overflow: hidden;
    background: var(--page-bg);
  }
  .cover {
    position: absolute;
    left: 20px;
    top: 415px;
    width: 1000px;
    height: 369px;
    display: block;
  }
  .serif { font-family: "Tinos", "Times New Roman", serif; }
  .display { font-family: "Anton", "Impact", sans-serif; }
</style>
</head>
<body>
<svg class="cover" viewBox="0 0 1159 428" xmlns="http://www.w3.org/2000/svg" aria-label="Vega Claims Billing cover banner">
  <defs>
    <linearGradient id="cover-bg" x1="0" y1="0" x2="1" y2="1">
      <stop offset="0" stop-color="var(--cover-white)"/>
      <stop offset="1" stop-color="var(--cover-mist)"/>
    </linearGradient>
    <linearGradient id="band-fill" x1="0" y1="0" x2="1" y2="0">
      <stop offset="0" stop-color="var(--violet)"/>
      <stop offset="1" stop-color="var(--magenta)"/>
    </linearGradient>
    <linearGradient id="practice-fill" x1="0" y1="0" x2="1" y2="0">
      <stop offset="0" stop-color="#5b2a8e"/>
      <stop offset="1" stop-color="#a8429a"/>
    </linearGradient>
    <linearGradient id="photo-stethoscope" x1="0" y1="0" x2="1" y2="1">
      <stop offset="0" stop-color="#3d4f68"/>
      <stop offset="0.5" stop-color="#c7ccd3"/>
      <stop offset="1" stop-color="#eef0f2"/>
    </linearGradient>
    <linearGradient id="photo-touch" x1="0" y1="0" x2="0" y2="1">
      <stop offset="0" stop-color="#e9e6c8"/>
      <stop offset="0.45" stop-color="#c9a88e"/>
      <stop offset="1" stop-color="#4a3a36"/>
    </linearGradient>
    <linearGradient id="photo-notes" x1="0" y1="0" x2="1" y2="1">
      <stop offset="0" stop-color="#dfe5ee"/>
      <stop offset="0.6" stop-color="#c9d3e2"/>
      <stop offset="1" stop-color="#6b8ab8"/>
    </linearGradient>
    <filter id="frame-shadow" x="-20%" y="-20%" width="140%" height="140%">
      <feDropShadow dx="0" dy="3" stdDeviation="4" flood-color="#000" flood-opacity="0.25"/>
    </filter>
  </defs>

  <!-- background -->
  <rect class="cover-bg" width="1159" height="428" fill="url(#cover-bg)"/>

  <!-- brand name -->
  <g class="brand">
    <circle cx="86" cy="92" r="9" fill="var(--plum)"/>
    <text class="serif" x="102" y="101" font-size="25" fill="var(--plum)">Vega Claims Billing</text>
  </g>

  <!-- diagonal rule -->
  <g class="diagonal-rule" stroke="var(--navy)" stroke-width="2.5">
    <line x1="0" y1="353" x2="180" y2="263"/>
    <line x1="430" y1="140" x2="709" y2="0"/>
  </g>

  <!-- headline -->
  <g class="headline" transform="translate(300 205) rotate(-17)">
    <text class="serif" x="-95" y="-62" font-size="48" fill="var(--navy)">HELP YOUR</text>
    <text class="display" x="-170" y="22" font-size="96" fill="url(#practice-fill)" transform="skewX(-8)">PRACTICE</text>
    <text class="display" x="-70" y="90" font-size="72" fill="var(--navy)" transform="skewX(-8)">SUCCEED</text>
  </g>

  <!-- accent bars -->
  <g class="accents">
    <rect x="500" y="205" width="18" height="68" fill="var(--magenta)"/>
    <rect x="656" y="92" width="14" height="16" fill="var(--accent-blue)"/>
    <polyline points="640,290 668,284 668,318" fill="none" stroke="var(--plum)" stroke-width="5"/>
    <rect x="850" y="300" width="14" height="16" fill="var(--plum)"/>
    <rect x="1005" y="146" width="17" height="68" fill="var(--accent-blue)"/>
    <polyline points="980,275 1010,268 1010,240" fill="none" stroke="var(--plum)" stroke-width="5"/>
  </g>

  <!-- photo frames -->
  <g class="photos">
    <polygon points="519,142 676,108 677,295 520,330" fill="var(--cover-white)" filter="url(#frame-shadow)"/>
    <polygon role="img" aria-label="Photo of a stethoscope resting on a medical chart" points="528,150 668,118 668,287 528,318" fill="url(#photo-stethoscope)"/>

    <polygon points="676,70 849,44 849,325 677,372" fill="var(--cover-white)" filter="url(#frame-shadow)"/>
    <polygon role="img" aria-label="Close-up photo of a finger touching a tablet screen" points="685,78 840,53 840,318 685,363" fill="url(#photo-touch)"/>

    <polygon points="849,132 1003,99 1003,269 849,300" fill="var(--cover-white)" filter="url(#frame-shadow)"/>
    <polygon role="img" aria-label="Photo of a clinician writing notes on a clipboard" points="857,140 995,108 995,262 857,292" fill="url(#photo-notes)"/>
  </g>

  <!-- office hours -->
  <g class="hours serif" font-size="22" fill="var(--navy)">
    <text x="890" y="55">Monday - Friday</text>
    <text x="890" y="81">9:00am - 5:00pm PST</text>
  </g>

  <!-- contact band -->
  <g class="contact-band">
    <polygon points="0,354 469,354 507,428 0,428" fill="url(#band-fill)"/>
    <circle cx="97" cy="392" r="20" fill="var(--cover-white)"/>
    <path d="M89 381 c3 -2 5 -1 6 1 l2 5 c1 2 0 3 -2 4 c1 4 4 7 8 8 c1 -2 2 -3 4 -2 l5 2 c2 1 3 3 1 6 c-2 3 -6 4 -10 2 c-7 -3 -13 -9 -16 -16 c-2 -4 -1 -8 2 -10z" fill="var(--violet)"/>
    <text class="serif" x="132" y="409" font-size="44" font-style="italic" font-weight="700" fill="var(--cover-white)">(555) 318-0927</text>
    <text class="serif" x="519" y="401" font-size="22" fill="var(--navy)">WWW.VEGACLAIMSBILLING.COM</text>
    <rect x="505" y="423" width="654" height="5" fill="var(--pink-rule)"/>
  </g>
</svg>
</body>
</html>
```